Hope KLN Disease (Non-Profit) Tri-Fold Brochure Design

We have put together the content for a brochure that we will distribute to doctors, researchers and patients about our non-profit. We would like the design of the brochure to look more professional and have nice aesthetics. It needs to incorporate all of the content in the attached Word file. We will have printed once we have a finished design.

Target Market(s)

Medical

Industry/Entity Type

Non Profit

Font styles to use
Serif
Sans Serif

Colors
33a6d7

Requirements
Must have
• Must include all content provided. Professional.
Nice to have
• Colors

```html
<!DOCTYPE html>
<html lang="en">
<head>
<meta charset="utf-8">
<title>Hope KLN Disease – Tri-Fold Brochure</title>
<link href="https://fonts.googleapis.com/css2?family=Source+Sans+3:ital,wght@0,400;0,600;0,700;1,600;1,700&family=Roboto+Condensed:wght@400;700&family=Oswald:wght@500;600&family=Nunito:wght@800&display=swap" rel="stylesheet">
<style>
:root{
  --kraft:#a97a4e;
  --teal:#2fbac5;
  --teal-deep:#1c9cab;
  --navy-teal:#16637d;
  --blue:#33a6d7;
  --blue-mid:#2a9ad0;
  --mint:#6fcbb5;
  --sky:#62c6dc;
  --orange:#f7941d;
  --ink:#3b3b3b;
  --paper:#f4f5f6;
  --white:#ffffff;
}
*{margin:0;padding:0;box-sizing:border-box}
html,body{width:756px;height:1200px;overflow:hidden}
body{background:var(--kraft);font-family:"Source Sans 3",sans-serif;color:var(--ink);position:relative}
.side-label{position:absolute;width:225px;text-align:center;font-family:"Roboto Condensed",sans-serif;font-weight:700;font-size:21px;color:var(--white)}
.panel{position:absolute;width:225px;height:526px;overflow:hidden;box-shadow:0 2px 4px rgba(0,0,0,.35)}
.row-top{top:62px}.row-bottom{top:614px}
.col-a{left:44px}.col-b{left:269px}.col-c{left:494px}
.abs{position:absolute}
.body-text{font-size:7.2px;line-height:1.45;text-align:justify}
.body-text p{margin-bottom:6px}
.url{font-family:"Oswald",sans-serif;font-weight:600;letter-spacing:2.4px;color:var(--white)}
.photo{background:linear-gradient(160deg,#e9eef1,#c9d6de 55%,#aebfcb)}

/* side 6 */
.what{background:var(--teal);color:var(--white)}
.what h1{position:absolute;top:18px;width:100%;text-align:center;font-family:"Source Sans 3",sans-serif;font-weight:600;font-size:22px}
.what .intro{position:absolute;top:60px;left:21px;right:21px;font-size:7.2px;line-height:1.5;text-align:center}
.what .intro p{margin-bottom:7px}
.penetrance{position:absolute;top:208px;left:0;right:0;bottom:0;background:var(--paper);color:#222;text-align:center}
.penetrance h2{margin-top:20px;font-size:15px;font-weight:700}
.penetrance .lead{font-size:7.3px;margin:8px 16px 0;line-height:1.35}
.penetrance .key{font-size:7.3px;margin-top:9px;line-height:1.95}
.pie{position:absolute;left:0;top:0}
.pie-label{position:absolute;font-size:5.4px;line-height:1.1;color:#222;text-align:left;white-space:nowrap}

/* side 5 */
.support{background:var(--paper)}
.banner{position:absolute;top:109px;left:16px;width:205px;height:52px;background:var(--navy-teal);border-radius:4px;color:var(--white);text-align:center;font-family:"Source Sans 3",sans-serif}
.banner .big{font-size:19px;font-weight:600;margin-top:4px;line-height:1.15}
.banner .small{font-size:15px;font-weight:600;line-height:1.2}
.support h2{position:absolute;top:176px;width:100%;text-align:center;font-size:16px;font-weight:600;color:var(--blue-mid)}
.support .body-text{position:absolute;top:203px;left:13px;right:13px}
.callout{position:absolute;top:297px;left:15px;width:190px;height:56px;background:var(--orange);border-radius:6px;color:var(--white);text-align:center;font-size:7.2px;line-height:1.5;padding-top:5px}
.callout em,.callout b{font-weight:700}
.org{position:absolute;top:372px;width:100%;text-align:center}
.org h3{font-size:12.5px;font-weight:700;color:var(--blue-mid)}
.org p{font-size:8.4px;margin-top:4px;line-height:1.35}
.org .web{font-family:"Oswald",sans-serif;font-weight:600;letter-spacing:1.8px;color:var(--blue-mid);font-size:11px;margin-top:3px}
.mark{display:flex;align-items:center;gap:5px;font-weight:700;color:var(--blue)}
.mark .dot{border-radius:50%;background:var(--blue);flex:none}

/* side 1 */
.cover{background:linear-gradient(180deg,#f4f5f6 0%,#f4f5f6 68%,#8fd3dd 100%)}
.cover .mark{position:absolute;top:50px;left:0;right:0;justify-content:center;font-size:20px}
.cover .mark .dot{width:22px;height:22px}
.cover .question{position:absolute;top:145px;width:100%;text-align:center;font-family:"Roboto Condensed",sans-serif;font-weight:700;font-size:17px;line-height:1.2;color:var(--navy-teal)}
.bars{position:absolute;top:192px;left:0;width:100%}
.bar{height:21px;margin-bottom:3px;color:var(--white);text-align:center;font-family:"Roboto Condensed",sans-serif;font-weight:700;font-size:16px;line-height:21px}
.cover .consider{position:absolute;top:349px;left:14px;width:196px;height:76px;background:var(--navy-teal);border-radius:6px;color:var(--white);text-align:center;font-size:12px;font-weight:600;line-height:1.35;padding-top:5px}
.cover .expand{position:absolute;top:431px;width:100%;text-align:center;font-size:10.5px;line-height:1.45;color:#222}
.cover .url{position:absolute;top:492px;width:100%;text-align:center;font-size:17px}

/* side 2 */
.symptoms{background:var(--paper)}
.section-title{font-family:"Roboto Condensed",sans-serif;font-weight:700;font-size:16px;color:var(--blue-mid)}
.symptoms .section-title{position:absolute;top:22px;left:21px}
.symptoms .body-text{position:absolute;top:52px;left:21px;width:190px}
.symptoms .narrow{position:absolute;top:358px;left:21px;width:91px}
.symptoms .band{position:absolute;bottom:0;left:0;right:0;height:53px;background:var(--teal)}

/* side 3 */
.research{background:var(--teal);color:var(--white);text-align:center}
.research h2{position:absolute;top:22px;left:0;right:0;font-family:"Nunito",sans-serif;font-weight:800;font-size:19px;line-height:1.27}
.research h3{position:absolute;top:111px;width:100%;font-size:14px;font-weight:600}
.research .goal{position:absolute;top:138px;left:13px;right:13px;font-size:8.3px;line-height:1.45}
.research .cta{position:absolute;top:194px;left:16px;width:190px;height:93px;background:var(--orange);border-radius:8px;font-size:10.5px;font-weight:600;line-height:1.38;padding-top:7px}
.research .cta .big{font-size:14px;font-weight:700}
.research .go{position:absolute;top:308px;width:100%;font-size:11px;font-weight:600;line-height:1.3}
.research .go .url{font-size:15px;letter-spacing:2px;display:block}
.research .free{position:absolute;top:371px;left:12px;right:12px;font-size:10.4px;font-weight:700;line-height:1.35;color:#0e2f3a}
.research .plea{position:absolute;top:418px;left:12px;right:12px;font-size:8.2px;font-weight:700;font-style:italic;line-height:1.38;color:#0e2f3a}
.research .band{position:absolute;bottom:0;left:0;right:0;height:53px;background:linear-gradient(90deg,#ffffff 0%,#ffffff 45%,#d5e6ef 100%)}
.research .band .mark{position:absolute;left:18px;top:17px;font-size:12px;color:#44607a;font-weight:600}
.research .band .mark .dot{width:10px;height:10px;background:#8fa9bd}

/* side 4 */
.diagnosis{background:var(--paper)}
.diagnosis .section-title{font-weight:400;color:var(--blue-mid);font-size:14.5px}
.diagnosis .t1{position:absolute;top:22px;left:16px}
.diagnosis .d-text{position:absolute;top:47px;left:16px;right:20px;font-size:7.3px;line-height:1.45;text-align:justify}
.diagnosis .d-text p{margin-bottom:6px}
.diagnosis ul{list-style:none;margin-top:8px}
.diagnosis li{position:relative;padding-left:12px;margin-bottom:9px}
.diagnosis li::before{content:"";position:absolute;left:0;top:2px;width:5px;height:5px;border-radius:50%;background:var(--blue-mid)}
.structure{position:absolute;top:178px;left:0;right:0;height:164px;background:radial-gradient(circle at 45% 50%,#2a6fc4 0%,#153a7a 38%,#050a14 75%)}
.diagnosis .t2{position:absolute;top:358px;left:16px}
.diagnosis .t-text{position:absolute;top:385px;left:16px;right:20px;font-size:7.3px;line-height:1.45;text-align:justify}
.diagnosis .t-text p{margin-bottom:6px}
.diagnosis .band{position:absolute;top:472px;left:0;right:0;height:34px;background:var(--teal);text-align:center}
.diagnosis .band .url{font-size:17px;line-height:34px}
</style>
</head>
<body>

<div class="side-label" style="left:44px;top:24px">Side 6</div>
<div class="side-label" style="left:269px;top:24px">Side 5</div>
<div class="side-label" style="left:494px;top:24px">Side 1</div>

<!-- SIDE 6 -->
<section class="panel row-top col-a what">
  <h1>What is IBMPFD?</h1>
  <div class="intro">
    <p>Inclusion Body Myopathy associated with Paget's disease of bone and Frontotemporal Dementia is an autosomal dominant mutation in chromosome 9 of the VCP (Valosin Containing Protein) gene. Given the interaction with other genetic diseases, this mutation may also be known as VCP Disease or Disorder.</p>
    <p>Some patients have familial Amyotrophic Lateral Sclerosis (ALS or Lou Gehrig's disease) or Parkinson's which has been shown to have a pathogenic variant in VCP.</p>
  </div>
  <div class="penetrance">
    <h2>Penetrance by Phenotype</h2>
    <p class="lead">The frequency that IBMPFD or VCP Disease manifests itself in one, two, or three primary disorders.</p>
    <div class="key">
      <div><b>IBM:</b> Inclusion Body Myopathy</div>
      <div><b>PDB:</b> Paget's Disease of the Bone</div>
      <div><b>FTD:</b> Frontotemporal Dementia</div>
    </div>
  </div>
  <svg class="pie" width="225" height="526" viewBox="0 0 225 526" role="img" aria-label="Pie chart of penetrance by phenotype">
    <ellipse cx="122" cy="456" rx="95" ry="50" fill="#3a3a3a"/>
    <rect x="27" y="440" width="190" height="16" fill="#3a3a3a"/>
    <g transform="translate(122 440) scale(1 .526) rotate(-90)">
      <circle r="47.5" fill="none" stroke="#4472c4" stroke-width="95" pathLength="99" stroke-dasharray="10 89" stroke-dashoffset="0"/>
      <circle r="47.5" fill="none" stroke="#ed7d31" stroke-width="95" pathLength="99" stroke-dasharray="16 83" stroke-dashoffset="-10"/>
      <circle r="47.5" fill="none" stroke="#555555" stroke-width="95" pathLength="99" stroke-dasharray="37 62" stroke-dashoffset="-26"/>
      <circle r="47.5" fill="none" stroke="#fbbd19" stroke-width="95" pathLength="99" stroke-dasharray="27 72" stroke-dashoffset="-63"/>
      <circle r="47.5" fill="none" stroke="#5b9bd5" stroke-width="95" pathLength="99" stroke-dasharray="1 98" stroke-dashoffset="-90"/>
      <circle r="47.5" fill="none" stroke="#70ad47" stroke-width="95" pathLength="99" stroke-dasharray="5 94" stroke-dashoffset="-91"/>
      <circle r="47.5" fill="none" stroke="#264478" stroke-width="95" pathLength="99" stroke-dasharray="3 96" stroke-dashoffset="-96"/>
    </g>
  </svg>
  <div class="pie-label" style="left:102px;top:364px">FTD<br>only - 3%</div>
  <div class="pie-label" style="left:72px;top:368px">PDB<br>only - 5%</div>
  <div class="pie-label" style="left:136px;top:374px">IBM, PDB, and<br>FTD - 10%</div>
  <div class="pie-label" style="left:46px;top:380px">PDB &amp;<br>FTD - 1%</div>
  <div class="pie-label" style="left:188px;top:388px">IBM &amp; FTD<br>- 16%</div>
  <div class="pie-label" style="left:12px;top:393px">IBM &amp; PDB<br>- 27%</div>
  <div class="pie-label" style="left:180px;top:503px">IBM only - 37%</div>
</section>

<!-- SIDE 5 -->
<section class="panel row-top col-b support">
  <div class="abs photo" style="left:0;top:0;width:225px;height:148px" role="img" aria-label="Photo of a smiling doctor greeting a patient with a nurse in the background"></div>
  <div class="banner"><div class="big">Together We Can</div><div class="small">Make a Difference</div></div>
  <h2>PATIENT SUPPORT</h2>
  <p class="body-text">Hope KLN Disease, Inc. is a 501(c)(3) which was formed to drive efforts to cure diseases related to mutations of the Valosin Containing Protein (VCP) gene. Our main goal is to bring patients and doctors together so we can help one another and drive research towards a cure. We are also trying to bring awareness to the medical community about our rare disease.</p>
  <div class="callout">
    <em>We offer resources and support to patients,<br>caregivers and doctors. Connect with us.</em><br>
    <b>IBMPFD Community page, HopeKLN.org<br>IBMPFD-info.org</b>
  </div>
  <div class="org">
    <h3>Hope KLN Disease, Inc.</h3>
    <p>P.O. Box 4120, Millbrook, GA 30412<br><b>hopeklndisease@example.org</b></p>
    <p class="web">www.hopekln.org</p>
  </div>
  <div class="abs mark" style="left:16px;top:475px;font-size:11px"><span class="dot" style="width:12px;height:12px"></span>Hope KLN Disease</div>
  <div class="abs" style="left:150px;top:462px;width:58px;height:40px;background:#e6edf2;border:1px solid #c9d6df"></div>
</section>

<!-- SIDE 1 -->
<section class="panel row-top col-c cover">
  <div class="mark"><span class="dot"></span>Hope KLN Disease</div>
  <div class="question">Do you have a family<br>history of ADULT ONSET</div>
  <div class="bars">
    <div class="bar" style="background:var(--mint)">MUSCLE WEAKNESS?</div>
    <div class="bar" style="background:var(--sky)">DEMENTIA?</div>
    <div class="bar" style="background:var(--blue-mid)">BONE DISEASE?</div>
    <div class="bar" style="background:var(--teal-deep)">ALS?</div>
    <div class="bar" style="background:var(--sky)">PARKINSON'S?</div>
    <div class="bar" style="background:var(--blue-mid)">IBM?</div>
  </div>
  <div class="consider">You may consider talking to your doctor about a mutation of the VCP gene called IBMPFD</div>
  <p class="expand">Inclusion Body Myopathy associated<br>with Paget's Disease of Bone and<br>Frontotemporal Dementia.</p>
  <div class="url">www.hopekln.org</div>
</section>

<!-- SIDE 2 -->
<section class="panel row-bottom col-a symptoms">
  <h2 class="section-title">SYMPTOMS:</h2>
  <div class="body-text">
    <p>IBMPFD, a VCP Disease, is an adult onset disorder that can affect the muscles, bones, and brain, and an affected patient may have any combination of the following conditions:</p>
    <p>Inclusion Body Myopathy: The first symptom of IBMPFD is often muscle weakness (myopathy). Typically, patients first notice difficulty raising arms, losing balance or difficulty climbing stairs. As the disorder progresses, weakness develops in the other muscles in the arms, legs and core muscles. Muscle weakness can also affect respiratory and heart (cardiac) muscles. This disorder may first present in an individual's late 30's and over time occurs in approximately 90% of individuals with VCP Disease.</p>
    <p>Paget's disease of bone: Bone pain, particularly in the hips and spine, is usually the major symptom of Paget's disease. It most often affects bones of the hips, spine, and skull, and the long bones of the arms and legs. Paget's disease affects half of individuals with VCP Disease and typically first presents in a person's 30's or 40's, which is a much earlier age than those without VCP Disease.</p>
    <p>Frontotemporal Dementia: In about one-third of people with VCP Disease, the disorder also affects the brain. FTD typically changes personality, behavior, language and speech. FTD typically presents in the<br>mid-50's.</p>
  </div>
  <p class="body-text narrow">Amyotrophic Lateral Sclerosis (ALS or Lou Gehrig's disease): ALS occurs in approximately 10% of individuals with VCP Disease. Symptoms include increased muscle tone, weakness, muscle wasting, muscle</p>
  <div class="band"></div>
  <div class="abs photo" style="left:118px;top:340px;width:107px;height:186px;border-radius:50px 50px 0 0;background:linear-gradient(180deg,#c98f6a 0%,#e8d2c4 30%,#a9dce6 60%,#7fc7d8 100%)" role="img" aria-label="Photo of a smiling nurse in scrubs holding a clipboard"></div>
</section>

<!-- SIDE 3 -->
<section class="panel row-bottom col-b research">
  <h2>Strength through<br>numbers will help US<br>find a CURE!</h2>
  <h3>RESEARCH:</h3>
  <p class="goal">The goal of the RareLink registry is to connect as many patients and researchers as possible to help advance treatments and cures for rare diseases.</p>
  <div class="cta">If you have been diagnosed with IBMPFD or VCP Disease, please help us by <i><b>COMPLETING THE</b></i><br><span class="big">PATIENT REGISTRY</span><br>through <span class="big">RareLink.</span></div>
  <div class="go">Go to our website<span class="url">www.hopekln.org</span>to access the RareLink Registry</div>
  <p class="free">The RareLink registry is<br>free for patients to enroll and for<br>researchers to access.</p>
  <p class="plea">Please elect for researchers to have access to your registry, as that will greatly assist in the drive for a cure, especially when drug trials are recruiting patients.</p>
  <div class="band"><div class="mark"><span class="dot"></span>RareLink Registry</div></div>
</section>

<!-- SIDE 4 -->
<section class="panel row-bottom col-c diagnosis">
  <h2 class="section-title t1">DIAGNOSIS:</h2>
  <div class="d-text">
    <p>The only way of diagnosing VCP Disease is through genetic testing. Consult with your doctor about testing for mutations of the VCP gene.</p>
    <p>For information about genetic testing, our two medical advisors are available as resources:</p>
    <ul>
      <li>Dr. Helena Marsh, Medical Geneticist at University of Westbrook, hmarsh@westbrook.edu</li>
      <li>Dr. Paul Lindqvist, Neuromuscular Specialist at Eastfield University, plindqvist@eastfield.edu</li>
    </ul>
  </div>
  <div class="structure" role="img" aria-label="Ribbon model of the VCP protein structure showing the N-domain, linker and D1 ATPase domain"></div>
  <h2 class="section-title t2">TREATMENTS:</h2>
  <div class="t-text">
    <p>There is an approved treatment for Paget's disease of bone, so early testing for this disorder is very important.</p>
    <p>There are no known cures or treatments for the Inclusion Body Myopathy or Frontotemporal Dementia. Consult with your doctor about physical therapy, stretching, diet and mobility</p>
  </div>
  <div class="band"><span class="url">www.hopekln.org</span></div>
</section>

<div class="side-label" style="left:44px;top:1150px">Side 2</div>
<div class="side-label" style="left:269px;top:1150px">Side 3</div>
<div class="side-label" style="left:494px;top:1150px">Side 4</div>

</body>
</html>
```